Business Card Design

We sell fish products to corporate food companies who then turn these products into final food products for consumers

Industry/Entity Type

Business

Contact Information for Business Card

I need a corporate business card template for a fish products business. We would like it be professional for use in dealing with multi national companies. This company business card template will be used by multiple employees so the following fields must be open to edit (Name, Phone Number and Email address)

```html
<!DOCTYPE html>
<html lang="en">
<head>
<meta charset="utf-8">
<title>Tidewater Harvest – Business Card</title>
<link rel="stylesheet" href="https://fonts.googleapis.com/css2?family=Roboto:wght@300;400;700&display=swap">
<style>
  :root {
    --page-bg: #e9eaeb;
    --card-top: #e2edf0;
    --card-bottom: #d3e3e8;
    --brand-blue: #2b5fae;
    --text-blue: #3a6db3;
    --accent-green: #5fbf8f;
    --mark-blue: #2f7fc4;
  }
  * { box-sizing: border-box; margin: 0; padding: 0; }
  html, body {
    width: 1200px;
    height: 1000px;
    overflow: hidden;
    background: var(--page-bg);
    font-family: "Roboto", Arial, sans-serif;
  }
  .business-card {
    position: absolute;
    left: 180px;
    top: 260px;
    width: 840px;
    height: 480px;
    background: linear-gradient(160deg, var(--card-top), var(--card-bottom));
    box-shadow: 0 10px 30px rgba(0,0,0,0.12);
  }
  .brand {
    position: absolute;
    left: 150px;
    top: 150px;
    display: flex;
    align-items: center;
    gap: 16px;
  }
  .brand-dot {
    width: 52px;
    height: 52px;
    border-radius: 50%;
    background: var(--mark-blue);
  }
  .brand-name {
    font-size: 34px;
    font-weight: 400;
    color: var(--brand-blue);
    letter-spacing: 0.5px;
    line-height: 1.05;
  }
  .contact {
    position: absolute;
    left: 510px;
    top: 150px;
    list-style: none;
    font-size: 19px;
    font-weight: 300;
    color: var(--text-blue);
  }
  .contact-item {
    display: flex;
    align-items: center;
    gap: 10px;
    margin-bottom: 10px;
  }
  .contact-icon {
    width: 16px;
    height: 16px;
    fill: none;
    stroke: var(--accent-green);
    stroke-width: 1.6;
  }
  .holder {
    position: absolute;
    left: 150px;
    top: 290px;
    color: var(--brand-blue);
  }
  .holder-name {
    font-size: 44px;
    font-weight: 300;
    letter-spacing: 0.5px;
    line-height: 1;
  }
  .holder-title {
    font-size: 26px;
    font-weight: 700;
    margin-top: 4px;
  }
</style>
</head>
<body>
  <section class="business-card">
    <div class="brand">
      <span class="brand-dot"></span>
      <span class="brand-name">TIDEWATER<br>HARVEST</span>
    </div>

    <ul class="contact">
      <li class="contact-item">
        <svg class="contact-icon" viewBox="0 0 16 16" aria-hidden="true">
          <rect x="1.5" y="3.5" width="13" height="9" rx="1"/>
          <path d="M1.5 4 L8 9 L14.5 4"/>
        </svg>
        <span class="contact-email">JaneDoe@tidewaterharvest.com</span>
      </li>
      <li class="contact-item">
        <svg class="contact-icon" viewBox="0 0 16 16" aria-hidden="true">
          <path d="M4 1.5 L6 5 L4.5 6.5 C5.5 8.5 7.5 10.5 9.5 11.5 L11 10 L14.5 12 L13 14.5 C7 14 2 9 1.5 3 Z"/>
        </svg>
        <span class="contact-phone">+ 0000 000 0000</span>
      </li>
    </ul>

    <div class="holder">
      <p class="holder-name">JANE DOE</p>
      <p class="holder-title">General Manager</p>
    </div>
  </section>
</body>
</html>
```